Interior Decorating business - Logo & Stationery

"Velmora Spaces" is a newly established interior decorating company, based in Sydney, providing interior decorating, colour consulting and property styling services to residential and commercial clients.

We require a logo and stationery design (double-sided business card, A4 letterhead and with compliments slip (210mm X 95mm))

Letterhead information and with compliments slip:
Address - 9/31-33 Tindale Rd, Garrow Point NSW 2047
Phone - (02)9617 4082
Mobile - 0428 305 961
Email - nadia@velmoraspaces.com.au
Web - www.velmoraspaces.com.au
ABN - 47839205164

Business Cards should be double sided and are to include;
Nadia Kowal
Director

with email address, mobile number, website as listed above

They also need to include services offered i.e. Interior Decorating, Colour Consulting, Property Styling

Please note that the current content on the website will be updated, so disregard logo and content currently on the website.

Target Market(s)

Target market is two-fold - residential clients (primarily homeowners with pride in their homes) and commerical clients (specifically business owners of retail shops and cafes and property developers)

Industry/Entity Type

Residential

```html
<!DOCTYPE html>
<html lang="en">
<head>
<meta charset="utf-8">
<title>Velmora Spaces – Stationery</title>
<link rel="stylesheet" href="https://fonts.googleapis.com/css2?family=Arimo:wght@400&display=swap">
<style>
  :root {
    --paper: #ffffff;
    --ink: #4a4a50;
    --text: #444444;
    --teal: #1b8a93;
    --edge: #cfcfcf;
    --shadow: rgba(0, 0, 0, 0.55);
  }
  * { margin: 0; padding: 0; box-sizing: border-box; }
  html, body {
    width: 1200px; height: 900px; overflow: hidden;
    background: var(--paper);
    font-family: "Arimo", Arial, sans-serif;
    color: var(--text);
  }
  .canvas { position: relative; width: 1200px; height: 900px; }

  .sheet {
    position: absolute;
    background: var(--paper);
    border: 1px solid var(--edge);
    box-shadow: 7px 7px 4px var(--shadow);
  }

  /* Letterhead */
  .letterhead { left: 571px; top: 25px; width: 600px; height: 850px; }
  .letterhead .brand { position: absolute; left: 56px; top: 89px; display: flex; align-items: center; gap: 10px; }
  .letterhead .brand-mark { width: 26px; height: 26px; background: var(--teal); }
  .letterhead .brand-name { font-size: 24px; color: var(--ink); white-space: nowrap; }
  .letterhead .divider { position: absolute; left: 370px; top: 59px; width: 4px; height: 92px; background: var(--teal); }
  .letterhead .contact { position: absolute; left: 391px; top: 57px; font-size: 10.5px; line-height: 12px; color: var(--text); }
  .letterhead .contact p + p { margin-top: 12px; }
  .letterhead .services {
    position: absolute; left: 0; right: 0; top: 785px;
    text-align: center; font-size: 10.2px; color: var(--teal);
  }

  /* Compliments slip */
  .slip { left: 35px; top: 358px; width: 1103px; height: 325px; border-bottom: none; }
  .slip .brand { position: absolute; left: 105px; top: 162px; display: flex; align-items: center; gap: 16px; }
  .slip .brand-mark { width: 50px; height: 50px; background: var(--teal); }
  .slip .brand-name { font-size: 42px; color: var(--ink); white-space: nowrap; }
  .slip .divider { position: absolute; left: 683px; top: 106px; width: 6px; height: 170px; background: var(--teal); }
  .slip .contact { position: absolute; left: 721px; top: 101px; font-size: 18.5px; line-height: 22.5px; color: var(--text); }
  .slip .contact p + p { margin-top: 22px; }
</style>
</head>
<body>
<main class="canvas">

  <section class="sheet letterhead" aria-label="A4 letterhead">
    <div class="brand">
      <span class="brand-mark"></span>
      <span class="brand-name">Velmora Spaces</span>
    </div>
    <span class="divider"></span>
    <div class="contact">
      <p>9/31-33 Tindale Rd,<br>Garrow Point NSW 2047</p>
      <p>T&nbsp; 02 9617 4082<br>E&nbsp; nadia@velmoraspaces.com.au<br>W velmoraspaces.com.au</p>
      <p>ABN 47 839 205 164</p>
    </div>
    <p class="services">Interior Decorating | Colour Consulting | Property Styling</p>
  </section>

  <section class="sheet slip" aria-label="With compliments slip">
    <div class="brand">
      <span class="brand-mark"></span>
      <span class="brand-name">Velmora Spaces</span>
    </div>
    <span class="divider"></span>
    <div class="contact">
      <p>9/31-33 Tindale Rd,<br>Garrow Point NSW 2047</p>
      <p>T&nbsp; 02 9617 4082<br>E&nbsp; nadia@velmoraspaces.com.au<br>W velmoraspaces.com.au</p>
      <p>ABN 47 839 205 164</p>
    </div>
  </section>

</main>
</body>
</html>
```